Need A Modern Website Design For ADSL2+ Provider

AIM: To sell affordable combined ADSL2+ Unlimited & phone line rentals to residential customers.

TYPE: This project is for DESIGN only (no code)

Source Files: I need all source files, fonts, images to be provided in ZIP format.

Logo: Existing (attached)

-Corporate Colours-
Black & Red (Same as Logo)
Others colours are fine as long as it looks corporate and modern.

-Pages-
Need another page to display our pricing plan

(1)Homepage Design
(2)Page to display our plans (needs to be in tables)
Example: http://lnkbrev.example/QwTr8k

-Pricing Plan-
(1) $59.95 / Month (Metro / City Areas)
(2) $79.95 / Month (Outside City Areas / Rural Areas)
Detailed Pricing plans is in PDF attached
Updates

Target Market(s)

Both male & female, Young & Old

Industry/Entity Type

Residential

Requirements
Must have
• + Graphic banner on the home page that shows our ADSL2+ combo plan for ADSL2+ Unlimited & Phone Line Rental for only $59.95

+ A box to allow customers to login to their account (username & password + login button)

+ Clearly display contact number
+ Button to sign up
+ Button to check service availability something like https://checkin.pelwara.example/wizard/

+ Button for Live Chat
+ Navigation menu
+ Social media icons Facebook, Google +, Twitter
+ Minimal text on homepage
+ Corporate & Friendly
Nice to have
• + Effective use of icons with corporate colours
+ Effective use of stockphotos
(use of people in photos would be nice)

+ Effective use of graphics to navigate people through the site and inform customers of specials,etc.
Should not have
• + Cluttered
+ Don’t want long scrolling homepage
+ Don’t want too much text on homepage 500 words is the estimate max.

```html
<!DOCTYPE html>
<html lang="en">
<head>
<meta charset="utf-8">
<title>Corvane – ADSL2+ Unlimited &amp; Phone Line Rental</title>
<link rel="stylesheet" href="https://fonts.googleapis.com/css2?family=Oswald:wght@300;400;500&family=Questrial&family=Open+Sans:wght@400;700&display=swap">
<style>
  :root{
    --red:#f2382b;
    --red-dark:#c81f16;
    --black:#0b0b0b;
    --ink:#111;
    --white:#fff;
    --grey-panel:#e4e4e4;
    --grey-foot:#e6e6e6;
    --yellow:#ffd633;
    --orange:#ff8c12;
    --gold:#ffb12b;
  }
  *{box-sizing:border-box;margin:0;padding:0}
  html,body{width:1145px;height:1200px;overflow:hidden;background:var(--white);font-family:Arial,Helvetica,sans-serif;color:var(--ink)}
  .page{position:relative;width:1145px;height:1200px}

  /* header */
  .site-header{position:absolute;left:0;top:0;width:1145px;height:93px;background:var(--white);border-bottom:2px solid var(--red)}
  .brand{position:absolute;left:53px;top:23px;display:flex;align-items:center;gap:12px}
  .brand-dot{width:46px;height:46px;border-radius:50%;background:var(--black)}
  .brand-name{font-family:'Oswald',sans-serif;font-weight:400;font-size:34px;letter-spacing:2px;color:var(--black)}
  .header-actions{position:absolute;left:506px;top:42px;display:flex;gap:7px}
  .pill{height:33px;padding:0 12px;border-radius:9px;background:var(--red);color:var(--white);font-family:'Oswald',sans-serif;font-weight:500;font-size:22px;line-height:33px;text-transform:uppercase;letter-spacing:-.3px}
  .call-box{position:absolute;right:14px;top:14px;text-align:left}
  .call-label{font-family:'Oswald',sans-serif;font-weight:300;font-size:16px;color:var(--black);letter-spacing:-.2px}
  .call-number{font-family:'Oswald',sans-serif;font-weight:500;font-size:40px;line-height:44px;color:var(--black);letter-spacing:-1px}

  /* nav */
  .main-nav{position:absolute;left:0;top:93px;width:1145px;height:50px;background:linear-gradient(#1a1a1a,#000)}
  .main-nav a{position:absolute;top:0;height:50px;line-height:50px;color:var(--white);text-decoration:none;font-size:17px}
  .main-nav a.is-active{left:29px;width:100px;background:var(--red);text-align:center}

  /* hero */
  .hero{position:absolute;left:0;top:143px;width:1145px;height:362px}
  .hero-photo{position:absolute;inset:0;background:linear-gradient(110deg,#3a3a3a 0%,#6b6b6b 40%,#9a9a9a 55%,#3b3b3b 80%,#222 100%)}
  .hero-offer{position:absolute;left:706px;top:0;width:402px;height:312px;background:rgba(20,20,20,.92);text-align:center}
  .hero-title{margin-top:28px;font-family:'Oswald',sans-serif;font-weight:500;font-size:45px;line-height:52px;color:#d8d8d8;letter-spacing:-.5px}
  .hero-price{margin-top:12px;font-size:27px;color:var(--gold)}
  .hero-button{display:inline-block;margin-top:20px;width:222px;height:42px;border-radius:5px;border:2px solid #8a1610;background:linear-gradient(#ff5a43,var(--red-dark));color:var(--white);font-family:'Open Sans',sans-serif;font-weight:700;font-size:16px;line-height:38px}

  /* content */
  .content{position:absolute;left:0;top:505px;width:1145px;height:542px;background:linear-gradient(#dcdfe2 0%,#fff 12%,#fff 80%,#e4e4e4 100%)}
  .section-title{position:absolute;font-family:'Questrial',sans-serif;font-weight:400;font-size:32px;color:var(--black);letter-spacing:-.3px;text-transform:uppercase}
  .login-box{position:absolute;left:37px;top:99px;width:519px;height:75px;border-radius:10px;background:var(--grey-panel)}
  .field{position:absolute;top:23px;height:31px;width:176px;border:1px solid #cfcfcf;border-radius:5px;background:var(--white);font-size:14px;color:#666;padding:7px 12px}
  .login-button{position:absolute;left:402px;top:23px;width:95px;height:31px;border-radius:4px;background:linear-gradient(#333,#000);color:var(--white);font-size:14px;text-align:center;line-height:31px}
  .about-text{position:absolute;left:43px;top:299px;width:520px;font-size:14px;line-height:17px;color:#111}
  .more-link{position:absolute;left:43px;top:412px;font-size:13.5px;color:var(--red)}

  .plan-card{position:absolute;top:110px;width:227px;height:299px;border-radius:11px;overflow:hidden;background:linear-gradient(160deg,var(--yellow) 0%,#ffc21e 45%,var(--orange) 100%);text-align:center;color:var(--white);box-shadow:-6px 4px 14px rgba(0,0,0,.25)}
  .plan-ribbon{position:absolute;left:0;top:0;width:60px;height:60px}
  .plan-name{margin-top:18px;font-family:'Oswald',sans-serif;font-weight:400;font-size:44px;line-height:54px;color:#1a1200}
  .plan-price{font-family:'Oswald',sans-serif;font-weight:300;font-size:38px;line-height:44px}
  .plan-perk{margin-top:4px;font-weight:700;font-size:20px;line-height:21px}
  .plan-rate{font-family:'Oswald',sans-serif;font-weight:300;color:#1a1200}
  .plan-rate.local{margin-top:20px;font-size:22px;padding-bottom:10px;border-bottom:1px solid #c96a00;margin-left:10px;margin-right:10px}
  .plan-rate.long{margin-top:10px;font-size:21px;line-height:24px}
  .plan-rate small{display:block;font-size:16px;line-height:18px}
  .plan-cta{position:absolute;top:422px;display:flex;align-items:center;gap:9px;font-family:'Oswald',sans-serif;font-weight:300;font-size:17px;color:var(--red)}

  /* footer */
  .social-band{position:absolute;left:0;top:1047px;width:1145px;height:48px;background:var(--black)}
  .social-dot{position:absolute;top:8px;width:33px;height:33px;border-radius:50%;background:#e8e8e8}
  .site-footer{position:absolute;left:0;top:1095px;width:1145px;height:105px;background:var(--grey-foot);text-align:center}
  .footer-links{margin-top:21px;font-size:15px;color:var(--black)}
  .footer-links span{margin:0 6px;color:#666}
  .copyright{margin-top:10px;font-size:12.5px;color:var(--red)}
</style>
</head>
<body>
<div class="page">

  <header class="site-header">
    <div class="brand"><div class="brand-dot"></div><div class="brand-name">CORVANE</div></div>
    <div class="header-actions">
      <div class="pill">Sign Up</div>
      <div class="pill">Check Availablity</div>
      <div class="pill">Live Chat</div>
    </div>
    <div class="call-box">
      <div class="call-label">TO FIND OUT MORE OR JOIN CALL</div>
      <div class="call-number">1300 55 18 40</div>
    </div>
  </header>

  <nav class="main-nav">
    <a class="is-active">Home</a>
    <a style="left:181px">About us</a>
    <a style="left:328px">Products and Services</a>
    <a style="left:581px">Pricing</a>
    <a style="left:712px">Specials</a>
    <a style="left:852px">Contact Us</a>
  </nav>

  <section class="hero">
    <div class="hero-photo" role="img" aria-label="Photo of network cables plugged in over a circuit board with fibre optic strands"></div>
    <div class="hero-offer">
      <h1 class="hero-title">ADSL2+ Unlimited<br>&amp; Phone Line RentaL</h1>
      <div class="hero-price">for only $59.95</div>
      <div class="hero-button">SUBSCRIBE PLAN</div>
    </div>
  </section>

  <main class="content">
    <h2 class="section-title" style="left:44px;top:50px">User Login</h2>
    <div class="login-box">
      <div class="field" style="left:17px">username</div>
      <div class="field" style="left:207px">password</div>
      <div class="login-button">LOGIN</div>
    </div>

    <h2 class="section-title" style="left:44px;top:233px">About Corvane</h2>
    <p class="about-text">Corvane’s Linkpak2+ broadband and telephone plan is for Unlimited Broad band, line rental and for all calls which go over those lines. The plan requires the ADSL 2+ service, the telephone line and the pre-selection service (long distance and fixed to mobile calls) to be bundled. The service comes with a Wifi modem which is free but it will cost you $24.95 for delivery and handling and is a mandatory part of the service.</p>
    <a class="more-link">more info</a>

    <h2 class="section-title" style="left:651px;top:48px">Linkpak2+ Plans</h2>

    <div class="plan-card" style="left:664px">
      <svg class="plan-ribbon" viewBox="0 0 60 60"><polygon points="0,0 60,0 0,60" fill="#e8261b"/><text x="17" y="26" transform="rotate(-45 17 26)" fill="#fff" font-family="Arial" font-weight="700" font-size="8">ON NET</text></svg>
      <div class="plan-name">Metro</div>
      <div class="plan-price">$59.95</div>
      <div class="plan-perk">Free Set Up and<br>WIFI Modem</div>
      <div class="plan-rate local">.18c per Local Calls</div>
      <div class="plan-rate long">.29c / minute<small>Long Distance Calls</small></div>
    </div>
    <div class="plan-card" style="left:891px">
      <svg class="plan-ribbon" viewBox="0 0 60 60"><polygon points="0,0 60,0 0,60" fill="#e8261b"/><text x="14" y="28" transform="rotate(-45 14 28)" fill="#fff" font-family="Arial" font-weight="700" font-size="8">OFF NET</text></svg>
      <div class="plan-name">Regional</div>
      <div class="plan-price">$79.95</div>
      <div class="plan-perk">Free Set Up and<br>WIFI Modem</div>
      <div class="plan-rate local">.18c per Local Calls</div>
      <div class="plan-rate long">.29c / minute<small>Long Distance Calls</small></div>
    </div>

    <div class="plan-cta" style="left:666px">
      <svg width="20" height="20" viewBox="0 0 20 20"><circle cx="10" cy="10" r="10" fill="#ff9a00"/><polygon points="8,5.5 14.5,10 8,14.5" fill="#fff"/></svg>SUBSCRIBE PLAN NOW
    </div>
    <div class="plan-cta" style="left:897px">
      <svg width="20" height="20" viewBox="0 0 20 20"><circle cx="10" cy="10" r="10" fill="#ff9a00"/><polygon points="8,5.5 14.5,10 8,14.5" fill="#fff"/></svg>SUBSCRIBE PLAN NOW
    </div>
  </main>

  <div class="social-band">
    <div class="social-dot" style="left:472px"></div>
    <div class="social-dot" style="left:515px"></div>
    <div class="social-dot" style="left:557px"></div>
    <div class="social-dot" style="left:599px"></div>
    <div class="social-dot" style="left:640px"></div>
  </div>

  <footer class="site-footer">
    <div class="footer-links">ABOUT US<span>·</span>PRODUCTS AND SERVICES<span>·</span>PRICING<span>·</span>SPECIALS<span>·</span>CONTACT US</div>
    <div class="copyright">© Copyright 2013 Corvane. All Rights Reserved</div>
  </footer>

</div>
</body>
</html>
```